Detail Shop Business card design

i need a business card design for my new detailing company called 'Brenner's Detail Shop'. i want an all black and white design . simple, direct and to the point. i want the designer to choose a fitting font to match the logothe front should have logo, address, phone and email and the back side should have a slogan and text indicating that we offer services on anything including cars, trucks, motorcycles and RVs. slogan will read "we take pride in your ride"
maybe also very small on the back side the IG icon with Brenners_Detail_Shop

phone 482.615.7734
address 7384 E Harlow Ave
Spokane WA 99342
email: BrennersDetail@quorvail.com

Target Market(s)

all ages , auto enthusiasts

Industry/Entity Type

Automotive

Contact Information for Business Card

the front should have logo, address, phone and email and the back side should have a slogan and text indicating that we offer services on anything including cars, trucks, motorcycles and RVs. slogan will read "we take pride in your ride"

phone 482.615.7734
address 7384 E Harlow Ave
Spokane WA 99342

Colors
000000
ffffff

Requirements
Must have
• bold font and very simple design with good spacing
Nice to have
• anything creative from the designer indicating we service any types of vehicles
Should not have
• any colors ,

```html
<!DOCTYPE html>
<html lang="en">
<head>
<meta charset="utf-8">
<title>Brenner's Detail Shop – Business Card</title>
<link rel="stylesheet" href="https://fonts.googleapis.com/css2?family=Oswald:wght@400;600&display=swap">
<style>
  :root {
    --ink: #000000;
    --ink-soft: #2b2b2b;
    --paper: #ffffff;
    --backdrop: #e6e6e6;
  }
  * { box-sizing: border-box; margin: 0; padding: 0; }
  html, body { width: 1200px; height: 800px; overflow: hidden; }
  body {
    background: var(--backdrop);
    font-family: "Oswald", sans-serif;
    color: var(--ink);
    display: flex;
    flex-direction: column;
    align-items: center;
    justify-content: center;
    gap: 40px;
  }
  .card {
    width: 630px;
    height: 360px;
    background: var(--paper);
    box-shadow: 0 6px 18px rgba(0,0,0,0.12);
    position: relative;
  }
  .brand {
    display: flex;
    align-items: center;
    gap: 16px;
  }
  .brand-dot {
    width: 34px;
    height: 34px;
    border-radius: 50%;
    background: var(--ink);
    flex: none;
  }
  .brand-name {
    font-weight: 600;
    font-size: 34px;
    line-height: 1.1;
    text-transform: uppercase;
    color: var(--ink);
  }
  .card-front {
    display: flex;
    align-items: center;
    justify-content: center;
  }
  .card-back {
    display: flex;
    align-items: center;
    justify-content: space-between;
    padding: 0 50px 0 46px;
  }
  .card-back .brand-name { font-size: 28px; }
  .card-back .brand-dot { width: 28px; height: 28px; }
  .details { width: 255px; }
  .slogan {
    font-weight: 600;
    font-size: 27px;
    line-height: 1.05;
    color: var(--ink-soft);
  }
  .services {
    font-size: 12px;
    line-height: 1.3;
    color: var(--ink-soft);
    margin: 6px 0 26px;
  }
  .contact-list { list-style: none; }
  .contact-list li {
    display: flex;
    align-items: flex-start;
    gap: 10px;
    font-size: 15px;
    line-height: 1.3;
    color: var(--ink-soft);
    margin-bottom: 7px;
  }
  .contact-list svg { width: 13px; height: 13px; flex: none; margin-top: 4px; fill: var(--ink-soft); }
  .contact-list .social { font-size: 13px; }
</style>
</head>
<body>
  <section class="card card-front" aria-label="Card front">
    <div class="brand">
      <span class="brand-dot"></span>
      <span class="brand-name">Brenner's Detail Shop</span>
    </div>
  </section>

  <section class="card card-back" aria-label="Card back">
    <div class="brand">
      <span class="brand-dot"></span>
      <span class="brand-name">Brenner's<br>Detail Shop</span>
    </div>
    <div class="details">
      <h1 class="slogan">We Take Pride<br>In Your Ride</h1>
      <p class="services">We offer services on anything including<br>cars, trucks, motorcycles and RVs.</p>
      <ul class="contact-list">
        <li>
          <svg viewBox="0 0 16 16" aria-hidden="true"><path d="M3.5 1 6 1.5 7 5 5.3 6.3a9 9 0 0 0 4.4 4.4L11 9l3.5 1 .5 2.5-1.8 2C7.5 14.6 1.4 8.5 1.5 2.8z"/></svg>
          <span>482.615.7734</span>
        </li>
        <li>
          <svg viewBox="0 0 16 16" aria-hidden="true"><path d="M1 3h14v10H1z M1.5 3.5 8 9l6.5-5.5" stroke="#fff" stroke-width="1.2"/></svg>
          <span>BrennersDetail@quorvail.com</span>
        </li>
        <li>
          <svg viewBox="0 0 16 16" aria-hidden="true"><path d="M8 1a5 5 0 0 0-5 5c0 3.6 5 9 5 9s5-5.4 5-9a5 5 0 0 0-5-5zm0 7a2 2 0 1 1 0-4 2 2 0 0 1 0 4z"/></svg>
          <span>7384 E Harlow Ave<br>Spokane WA 99342</span>
        </li>
        <li class="social">
          <svg viewBox="0 0 16 16" aria-hidden="true"><circle cx="8" cy="8" r="7"/></svg>
          <span>Brenners_Detail_Shop</span>
        </li>
      </ul>
    </div>
  </section>
</body>
</html>
```